Flyer Tally Desk Ledger Kit

Hi
Can you please design me a DL Flyer for: Tally Desk Ledger Kit
Info:
Starting a new Business ?
Want to save on bookkeeping fees for your existing business?

You can now save 1000's off bookkeeping fees by Doing it Yourself.

Using our Bookkeeper software you simply key in the information as you go.

We offer one on one training, backup and support.
We can assist you with BAS Preparation and Payrol Advice.

Add Modules as required:
Point of Sale Module
Jobs Management Module
Website Intergration Module

Fee set up assistance and training.

Lets get the ball rolling: 1300 462 815
www.tldlk.com.au
admin@tldlk.com.au (use the logo thing you made)

Target Market(s)

Small Business

Colors
ec1f27
f04a50
f59296
fcdcdc
ffffff

Requirements
Nice to have
• image/s related to bookkeeping

```html
<!DOCTYPE html>
<html lang="en">
<head>
<meta charset="utf-8">
<title>Tally Desk Ledger Kit – DL Flyer</title>
<link rel="stylesheet" href="https://fonts.googleapis.com/css2?family=Inter+Tight:wght@300;400;700;800&family=Montserrat:wght@800&family=Playfair+Display:wght@900&display=swap">
<style>
  :root {
    --red: #ec1f27;
    --red-soft: #f04a50;
    --ink: #5f5f5f;
    --panel: #666666;
    --white: #ffffff;
    --backdrop: #e4e8e7;
    --sticker-edge: #5a5a5a;
  }
  * { margin: 0; padding: 0; box-sizing: border-box; }
  html, body { width: 990px; height: 1200px; overflow: hidden; }
  body { background: var(--backdrop); font-family: "Inter Tight", Arial, sans-serif; position: relative; }

  .flyer { position: absolute; left: 72px; top: 0; width: 846px; height: 1200px; background: var(--white); overflow: hidden; }
  .flyer > * { position: absolute; }

  /* Headline banner */
  .hero { left: 36px; top: 37px; width: 774px; height: 370px; background: var(--red); border-radius: 23px; }
  .hero > * { position: absolute; color: var(--white); white-space: nowrap; }
  .hero__kicker { left: 38px; top: 39px; font-size: 84px; font-weight: 800; letter-spacing: -0.06em; line-height: 1; }
  .hero__title { left: 36px; top: 102px; font-size: 134px; font-weight: 800; letter-spacing: -0.065em; line-height: 1; }
  .hero__mark { left: 556px; top: -30px; font-family: "Playfair Display", Georgia, serif; font-weight: 900; font-size: 390px; line-height: 1; }
  .hero__rule { left: 40px; top: 241px; width: 524px; height: 1.5px; background: var(--white); opacity: .85; }
  .hero__sub { left: 40px; top: 254px; font-size: 42px; font-weight: 700; letter-spacing: -0.045em; line-height: 42px; }

  /* Savings statement */
  .savings { left: 53px; top: 425px; width: 740px; color: var(--ink); font-weight: 700; letter-spacing: -0.045em; white-space: nowrap; }
  .savings__lead { display: flex; align-items: baseline; gap: 8px; }
  .savings__lead span:first-child { font-size: 42px; }
  .savings__big { font-size: 72px; font-weight: 800; color: var(--red); letter-spacing: -0.055em; line-height: 1; }
  .savings__tail { font-size: 41px; line-height: 1; margin-top: 4px; letter-spacing: -0.055em; }
  .divider { left: 53px; top: 566px; width: 731px; height: 1.5px; background: var(--ink); }
  .intro { left: 53px; top: 578px; color: var(--ink); font-weight: 300; font-size: 34px; line-height: 34px; letter-spacing: -0.04em; }

  /* Services panel */
  .services { left: 36px; top: 664px; width: 774px; height: 355px; background: var(--panel); border-radius: 23px; color: var(--white); }
  .services > * { position: absolute; }
  .services__offer { left: 40px; top: 31px; font-size: 27px; font-weight: 300; line-height: 32px; letter-spacing: -0.035em; }
  .services__heading { left: 40px; top: 120px; font-size: 31px; font-weight: 700; letter-spacing: -0.045em; }
  .module-list { left: 40px; top: 172px; list-style: none; font-size: 33px; font-weight: 300; line-height: 42px; letter-spacing: -0.035em; }
  .module-list li { display: flex; align-items: center; }
  .module-list svg { width: 14px; height: 20px; margin-right: 23px; }

  .sticker { left: 535px; top: 778px; width: 288px; height: 170px; transform: rotate(-2deg); }
  .sticker__edge { position: absolute; inset: -3px -8px -8px -3px; border: 4px solid var(--sticker-edge); border-radius: 10px; background: var(--white); }
  .sticker__face { position: absolute; inset: 0; background: var(--white); border-radius: 8px; display: flex; align-items: center; justify-content: center; text-align: center;
    font-family: "Montserrat", Arial, sans-serif; font-weight: 800; color: var(--red); font-size: 39px; line-height: 37px; letter-spacing: -0.04em; }

  /* Call to action */
  .cta { left: 217px; top: 983px; width: 414px; height: 76px; }
  .cta__pill { position: absolute; inset: 0 0 12px 0; background: var(--red); border: 7px solid var(--white); border-radius: 40px; display: flex; align-items: center; justify-content: center;
    color: var(--white); font-size: 33px; font-weight: 700; letter-spacing: -0.045em; }
  .cta__pointer { position: absolute; left: 196px; bottom: 0; width: 22px; height: 14px; }

  /* Footer */
  .brand { left: 76px; top: 1102px; display: flex; align-items: center; gap: 12px; }
  .brand__dot { width: 40px; height: 40px; border-radius: 50%; background: var(--red); }
  .brand__name { font-size: 27px; font-weight: 700; color: var(--red); letter-spacing: -0.03em; }
  .footer-rule { left: 443px; top: 1082px; width: 1.5px; height: 92px; background: var(--ink); }
  .contact { left: 472px; top: 1080px; list-style: none; color: var(--ink); font-weight: 700; letter-spacing: -0.03em; }
  .contact li { display: flex; align-items: center; }
  .contact svg { width: 17px; height: 17px; margin-right: 10px; flex: none; }
  .contact__phone { font-size: 38px; line-height: 42px; }
  .contact__line { font-size: 26px; line-height: 30px; }
</style>
</head>
<body>
<main class="flyer">
  <section class="hero">
    <p class="hero__kicker">Starting a new</p>
    <h1 class="hero__title">Business</h1>
    <span class="hero__mark" aria-hidden="true">?</span>
    <div class="hero__rule"></div>
    <p class="hero__sub">Want to save on bookkeeping<br>fees for your existing business?</p>
  </section>

  <div class="savings">
    <p class="savings__lead"><span>You can now</span><span class="savings__big">Save 1000's Off</span></p>
    <p class="savings__tail">bookkeeping fees by “Doing it Yourself.”</p>
  </div>
  <div class="divider"></div>
  <p class="intro">Using our Bookkeeper software you simply key in the<br>information as you go.</p>

  <section class="services">
    <p class="services__offer">We offer one on one training, backup and support.<br>We can assist you with BAS Preparation and Payrol Advice.</p>
    <h2 class="services__heading">Add Modules as required:</h2>
    <ul class="module-list">
      <li><svg viewBox="0 0 14 20"><polyline points="3,3 11,10 3,17" fill="none" stroke="#fff" stroke-width="2.2"/></svg>Point of Sale Module</li>
      <li><svg viewBox="0 0 14 20"><polyline points="3,3 11,10 3,17" fill="none" stroke="#fff" stroke-width="2.2"/></svg>Jobs Management Module</li>
      <li><svg viewBox="0 0 14 20"><polyline points="3,3 11,10 3,17" fill="none" stroke="#fff" stroke-width="2.2"/></svg>Website Intergration Module</li>
    </ul>
  </section>

  <div class="sticker">
    <div class="sticker__edge"></div>
    <p class="sticker__face">Fee set up<br>assistance<br>and training.</p>
  </div>

  <div class="cta">
    <svg class="cta__pointer" viewBox="0 0 22 14"><polygon points="0,0 22,0 11,14" fill="#ec1f27"/></svg>
    <p class="cta__pill">Let’s get the ball rolling.</p>
  </div>

  <div class="brand">
    <span class="brand__dot"></span>
    <span class="brand__name">Tally Desk Ledger Kit</span>
  </div>
  <div class="footer-rule"></div>
  <ul class="contact">
    <li class="contact__phone"><svg viewBox="0 0 24 24"><path d="M6.5 3l3 4-2 2.5c1.2 2.6 3.4 4.8 6 6l2.5-2 4 3-2 3.5C11 19.5 4.5 13 3 5z" fill="none" stroke="#ec1f27" stroke-width="2" stroke-linejoin="round"/></svg>1300 462 815</li>
    <li class="contact__line"><svg viewBox="0 0 24 24"><rect x="2" y="5" width="20" height="14" fill="none" stroke="#ec1f27" stroke-width="2"/><polyline points="2,5 12,13 22,5" fill="none" stroke="#ec1f27" stroke-width="2"/></svg>admin@tldlk.com.au</li>
    <li class="contact__line"><svg viewBox="0 0 24 24"><circle cx="12" cy="12" r="10" fill="none" stroke="#ec1f27" stroke-width="2"/><ellipse cx="12" cy="12" rx="4.5" ry="10" fill="none" stroke="#ec1f27" stroke-width="2"/><line x1="2" y1="12" x2="22" y2="12" stroke="#ec1f27" stroke-width="2"/></svg>www.tldlk.com.au</li>
  </ul>
</main>
</body>
</html>
```